Bellhaven Select Business Card Design Project

About the company: Here at Marigrove Essence, we focus on cosmetic products that based on essential oils and different kinds of plant essences. All of our raw materials are pure organic and specially selected from local producers in Australia.

I'm here to look for a unique business card design, to replace the current one later on, so I don't have many requirements. Why I wanna restrict designers' creativity?

All I know is: 1. do not make it too complicated, straight forward, simple and pure. 2. this design may be used for other purposes (i.e. logo and slogan on the front, Brand Story and contact details at the back). Therefor, I'd like to have the design for 3 layouts, one only have logo, slogan, contact detials, one for the brand story, the other one for the personal business card with staff's mob etc...

A vector graphic is required, i.e. eps, ai, easy for me to resize.

Round Corner.

Thanks
Updates

Plz add "Hand made in Australia" in the design, cheers.

Target Market(s)

Women aged yr 20-50

Industry/Entity Type

Business

Requirements
Must have
• Logo: please see attacment (eps, ai)

Slogan: Dew Touched Delight

Website:www.marigroveessence-demo.com.au

Address: temporary not available

Phone: temporary not available

"Hand made in Australia"

Nice to have
• Prefer round corner

```html
<!DOCTYPE html>
<html lang="en">
<head>
<meta charset="utf-8">
<title>Marigrove Essence – Business Cards</title>
<link rel="stylesheet" href="https://fonts.googleapis.com/css2?family=Tinos:wght@400;700&display=swap">
<style>
  :root {
    --backdrop: #ece8e3;
    --card-cream: #f3efe6;
    --card-cream-deep: #e6e0d3;
    --ink: #2b2622;
    --rose: #e75c83;
    --rose-soft: #f2a7bb;
    --rose-pale: #fadbe4;
  }
  * { margin: 0; padding: 0; box-sizing: border-box; }
  html, body { width: 1200px; height: 697px; overflow: hidden; }
  body {
    background: var(--backdrop);
    font-family: "Tinos", "Times New Roman", serif;
    color: var(--ink);
  }
  .canvas {
    position: relative;
    width: 1200px;
    height: 697px;
    display: flex;
    align-items: center;
    justify-content: center;
    gap: 48px;
  }
  .card {
    position: relative;
    width: 540px;
    height: 300px;
    border-radius: 18px;
    overflow: hidden;
    background: radial-gradient(ellipse at 40% 30%, var(--card-cream) 0%, var(--card-cream) 55%, var(--card-cream-deep) 100%);
    box-shadow: 0 2px 10px rgba(0,0,0,0.12);
  }
  .card-swoosh {
    position: absolute;
    inset: 0;
    width: 100%;
    height: 100%;
  }
  .brand-mark {
    position: absolute;
    left: 150px;
    top: 30px;
    display: flex;
    align-items: center;
    gap: 8px;
    color: var(--rose);
    font-size: 24px;
    font-weight: 400;
  }
  .brand-dot {
    width: 12px;
    height: 12px;
    border-radius: 50%;
    background: var(--rose);
  }
  .card-details {
    position: absolute;
    left: 0;
    width: 470px;
    top: 82px;
    text-align: center;
  }
  .slogan {
    font-size: 14px;
    font-weight: 700;
    letter-spacing: 3px;
    text-transform: uppercase;
  }
  .contact {
    margin-top: 10px;
    font-size: 12.5px;
    line-height: 1.35;
  }
  .origin {
    margin-top: 18px;
    font-size: 17px;
    letter-spacing: 5px;
    text-transform: uppercase;
  }
  .rose-art {
    position: absolute;
    right: 40px;
    bottom: -40px;
    width: 210px;
    height: 190px;
    border-radius: 50% 46% 40% 50%;
    background: radial-gradient(circle at 45% 40%, var(--rose-pale) 0%, var(--rose-soft) 45%, var(--rose) 100%);
  }
</style>
</head>
<body>
<main class="canvas">
  <section class="card card-front">
    <svg class="card-swoosh" viewBox="0 0 540 300" aria-hidden="true">
      <path d="M470 6 C 560 60, 520 150, 440 200 C 360 250, 200 250, 0 282"
            fill="none" stroke="var(--rose)" stroke-width="5" stroke-linecap="round"/>
    </svg>
    <div class="brand-mark">
      <span class="brand-name">Marigrove</span>
      <span class="brand-dot"></span>
    </div>
    <div class="card-details">
      <p class="slogan">Dew Touched Delight</p>
      <p class="contact">
        Website:www.marigroveessence-demo.com.au<br>
        Address: 4780 2210 st NW Lake Town<br>
        Phone: 987654321
      </p>
      <p class="origin">Hand Made in Australia</p>
    </div>
  </section>

  <section class="card card-back">
    <svg class="card-swoosh" viewBox="0 0 540 300" aria-hidden="true">
      <path d="M0 40 C 140 60, 260 130, 340 180 C 400 215, 470 225, 540 215"
            fill="none" stroke="var(--rose)" stroke-width="5" stroke-linecap="round"/>
    </svg>
    <div class="rose-art" role="img" aria-label="Illustration of a pink rose in bloom"></div>
  </section>
</main>
</body>
</html>
```